Business Card Design

I design and sell kitchens. I would like the card to have a black background either gloss or matt and a stripe through the middle in deep sky blue, the same blue as the team ridgeway pro cycling team. Written in the blue stripe in white i would like Harbourline kitchens in italics. underneath the stripe, again in white i would like 'the complete design and installation service. On the reverse i would like the following in simple black on white
Owen Tramley
07814 296540
email- owentramley@harbourlinekitchens-example.co.uk
Web- WWW.harbourlinekitchens-example.co.uk

I have added a copy of an initial idea for a logo but it can be changed to suit the brief above

Industry/Entity Type

Business

Contact Information for Business Card

Harbourline Kitchens
The complete design and installation service
Owen Tramley
07814 296540-mob
owentramley@harbourlinekitchen-example.co.uk
WWW.harbourlinekitchens-example.co.uk

```html
<!DOCTYPE html>
<html lang="en">
<head>
<meta charset="utf-8">
<title>Harbourline Kitchens – Business Card</title>
<link rel="stylesheet" href="https://fonts.googleapis.com/css2?family=PT+Sans:ital,wght@0,400;0,700;1,400;1,700&display=swap">
<style>
  :root {
    --backdrop: #c0c0c0;
    --card-black: #231f1d;
    --sky-blue: #00a3d9;
    --white: #ffffff;
    --ink: #231f20;
  }
  * { margin: 0; padding: 0; box-sizing: border-box; }
  html, body {
    width: 1200px;
    height: 1200px;
    overflow: hidden;
    background: var(--backdrop);
    font-family: "PT Sans", "Helvetica Neue", Arial, sans-serif;
  }
  .sheet { position: relative; width: 1200px; height: 1200px; }

  .card {
    position: absolute;
    left: 241px;
    width: 716px;
    height: 472px;
    overflow: hidden;
  }

  /* Front */
  .card-front { top: 105px; background: var(--card-black); }
  .brand-stripe {
    position: absolute;
    left: 0; right: 0;
    top: 193px;
    height: 84px;
    background: var(--sky-blue);
    display: flex;
    align-items: center;
    justify-content: center;
  }
  .brand-name {
    color: var(--white);
    font-weight: 700;
    font-size: 48px;
    line-height: 1;
    letter-spacing: 0.2px;
  }
  .tagline {
    position: absolute;
    left: 0; right: 0;
    top: 297px;
    text-align: center;
    color: var(--white);
    font-weight: 700;
    font-style: italic;
    font-size: 24px;
    line-height: 1.2;
  }

  /* Back */
  .card-back { top: 623px; background: var(--white); }
  .back-band {
    position: absolute;
    left: 0; right: 0; top: 0;
    height: 53px;
    background: var(--card-black);
  }
  .contact {
    position: absolute;
    left: 0; right: 0;
    text-align: center;
    color: var(--ink);
    font-style: italic;
  }
  .person-name {
    top: 170px;
    font-weight: 700;
    font-size: 52px;
    line-height: 1;
  }
  .mobile {
    top: 237px;
    font-weight: 700;
    font-size: 30px;
    line-height: 1;
  }
  .online {
    top: 343px;
    font-weight: 400;
    font-size: 24px;
    line-height: 29px;
  }
</style>
</head>
<body>
  <main class="sheet">
    <section class="card card-front" aria-label="Card front">
      <div class="brand-stripe">
        <span class="brand-name">Harbourline kitchens</span>
      </div>
      <p class="tagline">the complete design and installation service</p>
    </section>

    <section class="card card-back" aria-label="Card back">
      <div class="back-band"></div>
      <p class="contact person-name">Owen Tramley</p>
      <p class="contact mobile">mob.: 07814 296540</p>
      <p class="contact online">
        email: owentramley@harbourlinekitchens-example.co.uk<br>
        Web: www.harbourlinekitchens-example.co.uk
      </p>
    </section>
  </main>
</body>
</html>
```